I want to revise my business card design and get a more modern and up to date design.

Brolvane Handyman Sevices originated from a family-owned and operated contractor business, performing home renovation, addition, and construction work in the NYC area since 2004. Today, we specialize in reliable and affordable handyman services for residential and commercial clients In 2014, we expanded to northern New Jersey. In 2016, we brought quality home improvement and repair services to new Bucks County, PA, and nearby New Jersey areas.
Target Market(s)
Home owners and business that might be looking for a General contractor, handyman, cleaning services and Home maintenance and property.
Industry/Entity Type
Construction Company
Contact Information for Business Card
I am open to new ideas
Colors
Designer to choose colors to be used in the design.
Look and feel
Each slider illustrates characteristics of the customer's brand and the style your logo design should communicate.

```html
<!DOCTYPE html>
<html lang="en">
<head>
<meta charset="utf-8">
<title>Brolvane Handyman Sevices – Business Card</title>
<link href="https://fonts.googleapis.com/css2?family=Fredoka:wght@600&family=Jost:wght@300;400;500&display=swap" rel="stylesheet">
<style>
  :root {
    --backdrop: #c8c8c8;
    --card-dark: #1c1c1c;
    --card-dark-glow: #3a3a3a;
    --card-light: #f2f2f2;
    --brand-red: #e8323a;
    --ink: #1a1a1a;
    --ink-soft: #555555;
    --rule: #3a3a3a;
  }
  * { margin: 0; padding: 0; box-sizing: border-box; }
  html, body { width: 1200px; height: 1200px; overflow: hidden; }
  body { background: var(--backdrop); position: relative; font-family: "Jost", sans-serif; }

  .card {
    position: absolute;
    left: 217px;
    width: 800px;
    height: 456px;
    overflow: hidden;
  }
  .card--front {
    top: 115px;
    background: radial-gradient(circle at 40% 30%, var(--card-dark-glow) 0%, var(--card-dark) 70%);
  }
  .card--back {
    top: 638px;
    background: var(--card-light);
  }

  .wordmark {
    font-family: "Fredoka", sans-serif;
    font-weight: 600;
    color: var(--brand-red);
    line-height: 1;
    position: absolute;
    letter-spacing: -1px;
  }
  .card--front .wordmark {
    right: 60px;
    top: 318px;
    font-size: 82px;
    color: #ffffff;
  }
  .card--front .brand-dot {
    position: absolute;
    width: 34px; height: 34px;
    border-radius: 50%;
    background: var(--brand-red);
    right: 438px;
    top: 350px;
  }

  .brand-block { position: absolute; right: 62px; top: 88px; text-align: left; }
  .brand-block .brand-square {
    position: absolute;
    left: -62px; top: 14px;
    width: 40px; height: 40px;
    background: var(--brand-red);
  }
  .card--back .wordmark {
    position: static;
    font-size: 70px;
    color: var(--ink);
  }
  .tagline {
    font-size: 14px;
    font-weight: 400;
    letter-spacing: 4.2px;
    color: var(--ink);
    margin-top: 4px;
    padding-left: 12px;
  }

  .contact { position: absolute; left: 52px; display: flex; align-items: center; gap: 22px; }
  .contact--phone { top: 270px; }
  .contact--mail { top: 362px; }
  .contact-icon { width: 40px; height: 40px; }
  .contact-text { font-size: 26px; font-weight: 300; color: var(--ink-soft); letter-spacing: 0.5px; }

  .name-rule {
    position: absolute;
    left: 3px; right: 2px;
    top: 322px;
    height: 1px;
    background: var(--rule);
  }
  .holder-name {
    position: absolute;
    right: 58px;
    top: 298px;
    padding: 0 8px;
    background: var(--card-light);
    font-size: 36px;
    font-weight: 500;
    color: var(--brand-red);
    letter-spacing: 1px;
    line-height: 1.3;
  }
</style>
</head>
<body>

  <section class="card card--front" aria-label="Business card front">
    <span class="brand-dot"></span>
    <div class="wordmark">Brolvane</div>
  </section>

  <section class="card card--back" aria-label="Business card back">
    <div class="brand-block">
      <span class="brand-square"></span>
      <div class="wordmark">Brolvane</div>
      <div class="tagline">HANDYMAN SERVICES</div>
    </div>

    <div class="contact contact--phone">
      <svg class="contact-icon" viewBox="0 0 40 40" aria-hidden="true">
        <circle cx="20" cy="20" r="18" fill="none" stroke="#1a1a1a" stroke-width="3"/>
        <path d="M13 11 l5 0 l2 6 l-3 2 q3 6 8 8 l2 -3 l6 2 l0 5 q-2 2 -5 2 q-10 -2 -16 -16 q0 -4 1 -6z" fill="#e8323a"/>
      </svg>
      <span class="contact-text">(215) 555-0184</span>
    </div>

    <div class="name-rule"></div>
    <div class="holder-name">MARCEL DUARTE</div>

    <div class="contact contact--mail">
      <svg class="contact-icon" viewBox="0 0 40 40" aria-hidden="true">
        <circle cx="20" cy="20" r="18" fill="none" stroke="#1a1a1a" stroke-width="3"/>
        <rect x="10" y="13" width="20" height="14" rx="1" fill="#e8323a"/>
        <path d="M10 13 l10 8 l10 -8" fill="none" stroke="#ffffff" stroke-width="1.6"/>
      </svg>
      <span class="contact-text">brolvanehandyman@mailbox.net</span>
    </div>
  </section>

</body>
</html>
```